RT Appraisals website redesign

I would like to refresh my existing website of www.rtappraisals.example with new graphics, look and feel, as well as updated structure and wording. Content and layout changes have been uploaded to this project Brief.

My existing website has a dark feel. I am now looking for a light and energetic feel. Financial Services is my industry, so the website should be reflect that. I would also like to reflect the concepts of Trust, Service and Expertise.

The website must be serious and upmarket.

Target Market(s)

Corporate board members, CFO's, treasurers and controllers
Auditors, tax advisors, private equity and venture capital asset managers, investors, tax authorities

Industry/Entity Type

Financial Service

Coding

Coded - Design and coding required

Number of Pages Required

5+ page

Font styles to use
Sans Serif
Other font styles liked:
• Designer can choose another modern font

Colors
0355a3
3277b5
85acd3
eaf1f7
f37122
f68d4d
9bcb3c
acd037
cadf82

Requirements
Must have
• Good hi resolution pictures that convey "Finance", "Trust", "Service" or "Expertise".
• An anti-bot (such as Captcha) mechanism in the contact form.
Should not have
• Must not have all content on one rolling screen.

```html
<!DOCTYPE html>
<html lang="en">
<head>
<meta charset="utf-8">
<title>RT Appraisals – Business &amp; Intellectual Property Valuations</title>
<link href="https://fonts.googleapis.com/css2?family=Montserrat:wght@500;600&family=Source+Sans+3:wght@300;400&display=swap" rel="stylesheet">
<style>
:root{
  --blue:#0a6cbb;
  --blue-deep:#0355a3;
  --blue-mid:#3277b5;
  --blue-light:#85acd3;
  --orange:#f37122;
  --orange-soft:#f68d4d;
  --ink:#1b1b1b;
  --grey:#555;
  --footer:#262626;
  --footer-deep:#161616;
  --white:#fff;
}
*{box-sizing:border-box;margin:0;padding:0}
html,body{width:1200px;height:2760px;overflow:hidden;background:var(--white)}
body{position:relative;font-family:"Source Sans 3",sans-serif;color:var(--ink)}
.abs{position:absolute}
h1,h2,h3,.nav,.topbar,.cta{font-family:"Montserrat",sans-serif}

/* top bar */
.topbar{left:0;top:0;width:1200px;height:46px;background:var(--blue);color:var(--white);font-size:14px;font-weight:500}
.topbar .item{position:absolute;top:14px;display:flex;align-items:center;gap:10px}
.topbar .divider{position:absolute;left:227px;top:12px;width:1px;height:22px;background:rgba(255,255,255,.7)}
.cta{position:absolute;left:837px;top:0;width:279px;height:46px;background:var(--orange);color:var(--white);font-size:13.5px;font-weight:600;display:flex;align-items:center;justify-content:center;letter-spacing:.2px}

/* header */
.header{left:0;top:46px;width:1200px;height:112px;background:var(--white)}
.brand{position:absolute;left:85px;top:26px;display:flex;align-items:center;gap:12px;font-family:"Montserrat",sans-serif;font-weight:500;font-size:22px;color:#333}
.brand .mark{width:22px;height:22px;border:2px solid #333}
.nav{position:absolute;right:86px;top:50px;display:flex;gap:0;font-size:14px;font-weight:600;color:#111}
.nav span{padding:0 19px}
.nav span.sep{padding:0}
.nav span:last-child{padding-right:0}

/* hero */
.hero{left:0;top:158px;width:1200px;height:503px;background:linear-gradient(100deg,#eef1f4 0%,#d5dbe2 30%,#b9a28d 48%,#6f7f93 70%,#2c3b52 100%)}
.hero h1{position:absolute;left:80px;top:216px;font-size:33px;font-weight:500;line-height:36px;color:#111;letter-spacing:.3px}

/* values */
.value{top:781px;width:300px;height:283px;background:var(--blue);color:var(--white);text-align:center}
.value .badge{position:absolute;left:91px;top:-62px;width:118px;height:118px;border-radius:50%;background:var(--white);border:3px solid var(--blue);display:flex;align-items:center;justify-content:center}
.value h2{margin-top:72px;font-size:22px;font-weight:500;letter-spacing:.3px}
.value p{margin:10px auto 0;width:262px;font-size:14.5px;line-height:26px}

/* services */
.services-photo{left:0;top:1138px;width:617px;height:672px;background:linear-gradient(135deg,#6d5e52 0%,#b8a58f 35%,#e4dcd2 60%,#c9d2dc 100%)}
.services-panel{left:617px;top:1138px;width:583px;height:672px;background:linear-gradient(180deg,var(--orange-soft),var(--orange))}
.svc-icon{width:86px;height:86px;border-radius:50%;background:var(--white);display:flex;align-items:center;justify-content:center;left:576px}
.svc{left:682px;width:430px;color:var(--white)}
.svc h3{font-size:25px;font-weight:500;margin-bottom:6px}
.svc p{font-size:14.5px;line-height:26px}
.ma{font-family:"Source Serif 4",Georgia,serif;color:var(--blue);font-size:24px;letter-spacing:-.5px}

/* coaching */
.coaching{left:85px;top:1888px;width:450px}
.coaching h3{font-size:24px;font-weight:500;color:#111;margin-bottom:12px}
.coaching p{font-size:16.5px;line-height:26px;color:var(--grey);font-weight:300}
.coaching-art{left:636px;top:1843px;width:478px;height:273px;background:radial-gradient(ellipse at 50% 60%,#dbe6f5 0%,#eef3fa 55%,#fff 80%)}

/* ppa */
.ppa{left:0;top:2150px;width:1200px;height:274px;background:linear-gradient(100deg,var(--blue-deep) 0%,#0c6ccc 55%,#2d8fd8 100%);color:var(--white);text-align:center}
.ppa h3{margin-top:52px;font-size:24px;font-weight:500}
.ppa p{margin:14px auto 0;width:1060px;font-size:17px;line-height:26px}

/* footer */
.footer{left:0;top:2424px;width:1200px;height:267px;background:var(--footer);color:var(--white)}
.footer h4{font-family:"Montserrat",sans-serif;color:var(--orange);font-size:21px;font-weight:600;position:absolute;top:42px}
.contact-row{position:absolute;left:85px;display:flex;gap:18px;font-size:15px;line-height:20px}
.links{position:absolute;left:475px;top:88px;width:210px;list-style:none;font-size:15px}
.links li{height:35px;display:flex;align-items:center;gap:10px;border-bottom:1px dashed #666}
.links li::before{content:"";width:5px;height:5px;border-radius:50%;background:#1a8fe0}
.partner{position:absolute;background:#3a3a3a;border-radius:4px}
.bottom{left:0;top:2691px;width:1200px;height:69px;background:var(--footer-deep);color:var(--white);font-size:15px}
.bottom .copy{position:absolute;left:86px;top:24px}
.social{position:absolute;right:86px;top:25px;display:flex;gap:14px}
.social span{width:16px;height:16px;border-radius:50%;background:var(--orange)}
</style>
</head>
<body>

<div class="abs topbar">
  <div class="item" style="left:86px">
    <svg width="16" height="16" viewBox="0 0 24 24"><path fill="#fff" d="M6.6 10.8a15 15 0 0 0 6.6 6.6l2.2-2.2c.3-.3.7-.4 1-.2 1.1.4 2.3.6 3.6.6.6 0 1 .4 1 1V20c0 .6-.4 1-1 1A17 17 0 0 1 3 4c0-.6.4-1 1-1h3.5c.6 0 1 .4 1 1 0 1.3.2 2.5.6 3.6.1.3 0 .7-.2 1z"/></svg>
    +31 70 555 0142
  </div>
  <div class="divider"></div>
  <div class="item" style="left:241px">
    <svg width="14" height="11" viewBox="0 0 14 11"><rect x="0.5" y="0.5" width="13" height="10" fill="none" stroke="#fff"/><path d="M.5 .5 7 6l6.5-5.5" fill="none" stroke="#fff"/></svg>
    info@rtappraisals.example
  </div>
  <div class="cta">SCHEDULE A FREE CONSULTATION</div>
</div>

<header class="abs header">
  <div class="brand"><span class="mark"></span>RT Appraisals</div>
  <nav class="nav">
    <span>HOME</span><span class="sep">|</span>
    <span>ABOUT</span><span class="sep">|</span>
    <span>SERVICES</span><span class="sep">|</span>
    <span>NEWS &amp; VIEWS</span><span class="sep">|</span>
    <span>CONTACT</span>
  </nav>
</header>

<section class="abs hero" role="img" aria-label="Business handshake photograph in front of a city skyline">
  <h1>BUSINESS &amp; INTELLECTUAL<br>PROPERTY VALUATIONS</h1>
</section>

<div class="abs value" style="left:85px">
  <div class="badge">
    <svg width="64" height="40" viewBox="0 0 64 40" fill="none" stroke="#f37122" stroke-width="3" stroke-linejoin="round"><path d="M4 6h14l10 6 8-4 10 0 14 0v18H50L38 36l-8-6-8 6-8-8H4z"/><path d="M28 12l-8 8 4 3 10-7"/></svg>
  </div>
  <h2>TRUST</h2>
  <p>Trust is paramount. Clients rely on RT Appraisals for confidentiality transparency and independence.</p>
</div>
<div class="abs value" style="left:449px">
  <div class="badge">
    <svg width="62" height="62" viewBox="0 0 62 62" fill="none" stroke="#f37122" stroke-width="2.5"><circle cx="31" cy="28" r="24"/><ellipse cx="31" cy="28" rx="11" ry="24"/><path d="M7 28h48M11 16h40M11 40h40"/><circle cx="20" cy="48" r="5" fill="#fff"/><circle cx="31" cy="50" r="5" fill="#fff"/><circle cx="42" cy="48" r="5" fill="#fff"/></svg>
  </div>
  <h2>SERVICE</h2>
  <p>Service is front and center at RT Appraisals. We consider the needs of all stakeholders and the personal needs of the client team involved.</p>
</div>
<div class="abs value" style="left:815px">
  <div class="badge">
    <svg width="64" height="58" viewBox="0 0 64 58" fill="none" stroke="#f37122" stroke-width="2.5"><circle cx="22" cy="10" r="6"/><circle cx="42" cy="10" r="6"/><circle cx="10" cy="30" r="6"/><circle cx="32" cy="30" r="7"/><circle cx="54" cy="30" r="6"/><circle cx="20" cy="48" r="6"/><circle cx="44" cy="48" r="6"/><path d="M25 15l4 8M39 15l-4 8M16 30h9M39 30h9M27 36l-4 7M37 36l4 7"/></svg>
  </div>
  <h2>EXPERTISE</h2>
  <p>Expertise is core to the philosophy of RT Appraisals. Our global network of professionals maintain and continue to develop the knowledge and experience that you expect from your trusted corporate finance partner.</p>
</div>

<section class="abs services-photo" role="img" aria-label="Photograph of a hand with a pen reviewing financial charts on a desk"></section>
<section class="abs services-panel"></section>

<div class="abs svc-icon" style="top:1182px">
  <svg width="46" height="46" viewBox="0 0 46 46" fill="#0a6cbb"><circle cx="9" cy="8" r="4"/><rect x="5" y="13" width="8" height="16"/><rect x="7" y="29" width="4" height="14"/><rect x="18" y="18" width="6" height="25"/><rect x="27" y="10" width="6" height="33"/><rect x="36" y="4" width="6" height="39"/><path d="M24 34l8-7 8 7v9H24z" fill="#f37122"/></svg>
</div>
<div class="abs svc" style="top:1182px">
  <h3>Business Valuation</h3>
  <p>Company stakeholders trust RT Appraisals to provide business valuations for transaction, accounting, tax, legal, and share or option participation purposes.<br>Through our bespoke approach and global network, we customize teams to the needs of our clients.</p>
</div>

<div class="abs svc-icon" style="top:1376px">
  <svg width="48" height="44" viewBox="0 0 48 44" fill="#0a6cbb"><path d="M4 44V30l10-6v20zM18 44V20l10-6v30zM32 44V10l12-8v42z"/></svg>
</div>
<div class="abs svc" style="top:1376px">
  <h3>Intellectual Property Valuation</h3>
  <p>Patents, unpatented technologies, know how, brands, trademarks, databases, customer-related assets - this is a limited sample of the wide universe of intellectual property that clients trust RT Appraisals to value. There are many techniques for valuing intellectual property and no two assets are alike.<br>Trust RT Appraisals for our expertise and client-centric approach.</p>
</div>

<div class="abs svc-icon" style="top:1595px"><span class="ma">M&amp;A</span></div>
<div class="abs svc" style="top:1593px">
  <h3>M&amp;A Advisory</h3>
  <p>Through our international network of M&amp;A professionals, RT Appraisals can assist companies with buying other companies or selling (parts of) their companies. RT Appraisals offers a flexible approach, assisting companies with part of the process or providing a full-service approach.</p>
</div>

<div class="abs coaching">
  <h3>Business Plan Coaching</h3>
  <p>Young companies and entrepreneurs frequently ask for our advice on their business plans and strategies.<br>With almost 2 decades of analyzing companies large and small, we are well positioned to advise companies based on experience and insight.</p>
</div>
<div class="abs coaching-art" role="img" aria-label="Illustration of a presenter at a flip chart addressing three seated business people"></div>

<section class="abs ppa">
  <h3>Purchase Price Allocation</h3>
  <p>Accounting procedures require an acquirer to allocate purchase consideration to the fair value of all acquired assets and liabilities when obtaining control of a company. This process, called a purchase price allocation (PPA), involves assets and liabilities that did not exist on the target’s balance sheet prior to the transaction. Certain pre-existing assets must be restated to fair value.<br>This process can be time consuming and complex. RT Appraisal Services has a wealth of experience in this area and can work with you and your independent auditor to achieve a smooth process.</p>
</section>

<footer class="abs footer">
  <h4 style="left:85px">CONTACT US</h4>
  <div class="contact-row" style="top:93px">
    <svg width="14" height="18" viewBox="0 0 14 18"><path d="M7 0a7 7 0 0 0-7 7c0 5 7 11 7 11s7-6 7-11a7 7 0 0 0-7-7z" fill="#1a8fe0"/><circle cx="7" cy="7" r="2.5" fill="#262626"/></svg>
    <span>Kanaalweg 48, 2321 JK Leiden<br>The Netherlands</span>
  </div>
  <div class="contact-row" style="top:157px">
    <svg width="16" height="16" viewBox="0 0 24 24"><path fill="#1a8fe0" d="M6.6 10.8a15 15 0 0 0 6.6 6.6l2.2-2.2c.3-.3.7-.4 1-.2 1.1.4 2.3.6 3.6.6.6 0 1 .4 1 1V20c0 .6-.4 1-1 1A17 17 0 0 1 3 4c0-.6.4-1 1-1h3.5c.6 0 1 .4 1 1 0 1.3.2 2.5.6 3.6.1.3 0 .7-.2 1z"/></svg>
    <span>+31 70 555 0142</span>
  </div>
  <div class="contact-row" style="top:198px">
    <svg width="16" height="12" viewBox="0 0 16 12"><rect width="16" height="12" fill="#1a8fe0"/><path d="M0 0l8 6 8-6" fill="none" stroke="#262626"/></svg>
    <span>info@rtappraisals.example</span>
  </div>

  <h4 style="left:475px">QUICK LINKS</h4>
  <ul class="links">
    <li>HOME</li><li>ABOUT</li><li>SERVICES</li><li>NEWS &amp; VIEWS</li>
  </ul>

  <div class="partner" style="left:916px;top:47px;width:198px;height:47px"></div>
  <div class="partner" style="left:934px;top:113px;width:180px;height:73px"></div>
</footer>

<div class="abs bottom">
  <div class="copy">© Copyright 2019 rtappraisals. All rights reserved.</div>
  <div class="social"><span></span><span></span><span></span></div>
</div>

</body>
</html>
```